Health and Wellness company needs flyer to promote free seminar

Stride reform studio is a health and wellness company that offers an exercise program designed by physical therapists to help relieve pain and improve mobility. Our business is a new concept that is not well understood by the public. In order to promote our business we offer a free seminar where we present information regarding the underlying cause of pain and tightness. During the seminar we also perform a posture screen and movement testing for all participants.

Target Market(s)

Mostly healthy and active women ages 25-65

Industry/Entity Type

Health And Wellness

Font styles to use
Sans Serif

Colors

Designer to choose colors to be used in the design.

Requirements
Must have
• Title: Eliminate Pain and Tightness For Good
• Paragraph: Stride Reform Studio offers a free 60 minute seminar: "The Busy Walker's Handbook to Bending and Standing Taller."
• What to Expect:
• • Identify the underlying cause of your pain and mobility issues
• • Expose what gets in the way of you moving and feeling better
• • Learn why traditional exercises don’t help and can actually make the problem worse
• • Reveal what your posture is saying and how that impacts you
• • Experience your muscle imbalances through movement tests
• • Discover the training method that realigns your posture, increases your mobility and reduces your pain
• Call to action: RSVP online at stridereformstudio.com
Nice to have
• Use a relevant image showing a female dealing with tightness in the low back, legs, etc.
• Emphasize that the seminar is FREE.
• Make the call to action prominent.

```html
<!DOCTYPE html>
<html lang="en">
<head>
<meta charset="UTF-8">
<title>Eliminate Pain and Tightness For Good – Stride Reform Studio</title>
<link href="https://fonts.googleapis.com/css2?family=Fjalla+One&family=Raleway:wght@400;500;700&display=swap" rel="stylesheet">
<style>
  :root {
    --violet: #5a5ea8;
    --lavender: #bcbde0;
    --ink: #3a3a3f;
    --paper: #ffffff;
    --backdrop: #ffffff;
    --accent: #f29a26;
    --sky-top: #a9d4ee;
    --sky-mid: #6cc3d8;
    --skin: #c98d6c;
    --garment: #f06fa2;
  }
  * { margin: 0; padding: 0; box-sizing: border-box; }
  html, body {
    width: 1200px; height: 887px; overflow: hidden;
    background: var(--backdrop);
  }
  .flyer {
    position: absolute; left: 287px; top: 0;
    width: 627px; height: 887px;
    background: var(--paper);
    overflow: hidden;
    font-family: "Raleway", Arial, sans-serif;
    color: var(--ink);
  }
  .flyer__shapes { position: absolute; inset: 0; }
  .headline {
    position: absolute; left: 37px; top: 38px;
    font-family: "Fjalla One", "Oswald", sans-serif;
    font-weight: 400; font-size: 62px; line-height: 88px;
    color: var(--paper); letter-spacing: -0.5px;
  }
  .brand {
    position: absolute; left: 38px; top: 380px;
    display: flex; align-items: center; gap: 10px;
    font-weight: 700; font-size: 24px; color: var(--violet);
  }
  .brand__mark {
    width: 40px; height: 40px;
    background: var(--accent);
  }
  .offer {
    position: absolute; left: 37px; top: 420px;
    font-family: "Fjalla One", "Oswald", sans-serif;
    font-size: 36px; color: var(--violet); line-height: 48px;
  }
  .seminar-title {
    position: absolute; left: 37px; top: 466px;
    font-size: 19px; font-weight: 500; color: var(--ink);
  }
  .expectations {
    position: absolute; left: 37px; top: 522px; width: 560px;
    list-style: none;
    font-size: 17.5px; line-height: 28.5px; color: var(--ink);
  }
  .expectations li::before { content: "•"; margin-right: 1px; }
  .cta {
    position: absolute; left: 83px; top: 756px;
    width: 460px; height: 460px; border-radius: 50%;
    background: var(--violet); color: var(--paper);
    text-align: center; padding-top: 26px;
  }
  .cta__label {
    font-family: "Fjalla One", "Oswald", sans-serif;
    font-size: 38px; line-height: 44px; display: block;
  }
  .cta__link { font-size: 19px; line-height: 24px; display: block; margin-top: 2px; white-space: nowrap; }
</style>
</head>
<body>
  <main class="flyer">
    <svg class="flyer__shapes" width="627" height="887" viewBox="0 0 627 887">
      <defs>
        <linearGradient id="hero-tones" x1="0" y1="0" x2="0" y2="1">
          <stop offset="0" stop-color="var(--sky-top)"/>
          <stop offset="0.45" stop-color="var(--sky-mid)"/>
          <stop offset="0.62" stop-color="var(--skin)"/>
          <stop offset="0.85" stop-color="var(--skin)"/>
          <stop offset="0.9" stop-color="var(--garment)"/>
          <stop offset="1" stop-color="var(--garment)"/>
        </linearGradient>
      </defs>
      <circle class="ring" cx="482" cy="140" r="290" fill="var(--lavender)"/>
      <circle class="hero-photo" cx="462" cy="104" r="290" fill="url(#hero-tones)"
              role="img" aria-label="Photo of an active woman in a sports top holding her lower back, beach and sea behind her"/>
      <circle class="title-disc" cx="100" cy="118" r="228" fill="var(--violet)"/>
    </svg>

    <h1 class="headline">Eliminate Pain<br>and Tightness<br>For Good</h1>

    <div class="brand"><span class="brand__mark"></span>stridereformstudio</div>

    <p class="offer">offers a free 60 minute seminar:</p>
    <p class="seminar-title">"The Busy Walker's Handbook to Bending and Standing Taller."</p>

    <ul class="expectations">
      <li>Identify the underlying cause of your pain and mobility issues</li>
      <li>Expose what gets in the way of you moving and feeling better</li>
      <li>Learn why traditional exercises don't help and can actually make the problem worse</li>
      <li>Reveal what your posture is saying and how that impacts you</li>
      <li>Experience your muscle imbalances through movement tests</li>
      <li>Discover the training method that realigns your posture, increases your mobility and reduces your pain</li>
    </ul>

    <div class="cta">
      <span class="cta__label">RSVP</span>
      <span class="cta__link">online at stridereformstudio.com</span>
    </div>
  </main>
</body>
</html>
```